Healthcare marketing Website design

This is for a healthcare marketing agency
All details and brief included in the files

I need the design to be incredible!

5 pages to be designed
Home page
About
Portfolio Page
Services
Start your project page

If you need more stock images - download preview images from kestrine pix so I can purchase at a later date

```html
<!DOCTYPE html>
<html lang="en">
<head>
<meta charset="utf-8">
<title>Clearpath Consulting — Healthcare Marketing Agency</title>
<link href="https://fonts.googleapis.com/css2?family=Libre+Franklin:ital,wght@0,400;0,500;0,600;0,700;1,400&display=swap" rel="stylesheet">
<style>
:root{
  --blue:#0ba3e3;
  --blue-soft:#dcf0fa;
  --navy:#2a3163;
  --footer:#252b4f;
  --ink:#2b2d3c;
  --body:#4a4d5c;
  --grey-soft:#f1f2f5;
  --white:#ffffff;
}
*{margin:0;padding:0;box-sizing:border-box}
html,body{width:1200px;height:3610px;overflow:hidden;background:var(--white)}
body{font-family:"Libre Franklin",Arial,sans-serif;color:var(--ink);position:relative}
.abs{position:absolute}
a{color:inherit;text-decoration:none}

.backdrop{position:absolute;left:0;top:0;width:1200px;height:3610px;z-index:0}
.page{position:absolute;left:0;top:0;width:1200px;height:3610px;z-index:1}

/* header */
.site-header{position:absolute;left:0;top:0;width:1200px;height:70px;z-index:5}
.brand{display:flex;align-items:center;gap:10px;font-weight:500;color:var(--blue);font-size:30px;letter-spacing:.5px}
.brand-dot{width:28px;height:28px;border-radius:50%;background:var(--blue)}
.nav{left:397px;top:25px;width:450px;height:20px;font-size:14px;font-weight:500;color:var(--ink)}
.nav a{position:absolute;top:0;white-space:nowrap}
.nav a.active{color:var(--blue)}
.social{width:34px;height:34px;border-radius:50%}
.social.navy{background:var(--navy)}
.social.blue{background:var(--blue)}
.btn{display:flex;align-items:center;justify-content:center;border-radius:20px;font-size:14px;font-weight:600;color:var(--white)}
.btn.blue{background:var(--blue)}
.btn.navy{background:var(--navy)}

/* hero */
.hero-art{z-index:1}
.hero-kicker{left:143px;top:234px;font-size:31px;color:var(--blue);font-weight:400;z-index:2}
.hero-title{left:143px;top:274px;font-size:46px;line-height:52px;font-weight:600;color:var(--ink);z-index:2}

/* shared */
.section-title{font-size:28px;line-height:31px;font-weight:500;color:var(--ink)}
.rule{height:1px;background:var(--blue);width:44px}
.photo{border-radius:14px 0 0 14px}
.frame{border:2px solid var(--blue);border-left:none;border-bottom:none;border-radius:0 14px 0 0}
.frame-l{border-left:2px solid var(--blue);}
.ticks{list-style:none;font-size:13px;color:var(--body);line-height:17px}
.ticks li{position:absolute;padding-left:26px;width:460px}
.ticks svg{position:absolute;left:0;top:4px}
.copy{font-size:13px;line-height:21.5px;color:var(--body)}
.copy-sm{font-size:11.2px;line-height:17px;color:var(--body)}

/* testimonial */
.quote-ring{width:82px;height:82px;border-radius:50%;border:2px solid var(--blue);display:flex;align-items:center;justify-content:center}
.quote-core{width:64px;height:64px;border-radius:50%;background:var(--blue);display:flex;align-items:center;justify-content:center}
.dot{width:13px;height:13px;border-radius:50%;border:1.5px solid var(--blue)}
.dot.on::after{content:"";display:block;width:5px;height:5px;background:var(--blue);border-radius:50%;margin:2.5px}

/* faq */
.faq{left:250px;width:700px}
.faq-row{position:absolute;left:0;width:700px;border-bottom:1px solid #e3e5ea;font-size:15px;font-weight:500;padding:0 14px;display:flex;align-items:center;justify-content:space-between}
.faq-plus{color:var(--blue);font-size:20px;font-weight:300}
.faq-open{background:var(--blue);color:var(--white);padding:12px 14px}

/* articles */
.card-img{height:194px}
.card-body{position:absolute;left:0;top:194px;width:268px;height:127px;border-right:2px solid var(--blue);background:var(--white)}
.card-title{position:absolute;left:29px;top:26px;font-size:15px;font-weight:500;color:var(--ink)}
.card-text{position:absolute;left:29px;top:56px;width:210px;font-size:11.5px;line-height:17px;color:var(--body)}

/* footer */
.footer{left:0;top:3197px;width:1200px;height:413px;background:var(--footer);color:var(--white)}
.foot-head{font-size:16px;font-weight:600;letter-spacing:.3px}
.foot-links{font-size:12.5px;line-height:21.3px;color:#e5e7f0}
</style>
</head>
<body>

<svg class="backdrop" viewBox="0 0 1200 3610" aria-hidden="true">
  <path d="M0 700 C120 690 330 780 430 1000 C500 1170 380 1380 150 1440 C90 1455 40 1455 0 1450 Z" fill="#e5f3fb"/>
  <path d="M1200 1640 L1200 2340 C1050 2260 920 2120 790 1980 C710 1890 700 1820 760 1780 C860 1720 1060 1670 1200 1640 Z" fill="#f1f2f5"/>
  <path d="M1200 1000 L1200 1420 C1140 1380 1080 1300 1080 1200 C1080 1100 1140 1030 1200 1000 Z" fill="#eef0f3"/>
  <path d="M0 2590 C180 2580 380 2620 450 2680 C480 2720 470 2760 420 2760 L0 2760 Z" fill="#e5f3fb"/>
</svg>

<main class="page">

  <!-- Hero art (sits below the header) -->
  <svg class="abs hero-art" style="left:477px;top:0" width="723" height="610" viewBox="0 0 723 610" role="img" aria-label="Photo of a doctor using a tablet with a glowing medical network overlay">
    <defs>
      <linearGradient id="heroGrad" x1="0" y1="0" x2="1" y2="1">
        <stop offset="0" stop-color="#f2f5f8"/>
        <stop offset=".35" stop-color="#c9d6e0"/>
        <stop offset=".65" stop-color="#c89b7e"/>
        <stop offset="1" stop-color="#6a7e93"/>
      </linearGradient>
    </defs>
    <path d="M723 0 L200 0 C160 40 60 200 25 300 C5 360 40 390 110 420 C260 480 420 540 560 590 C640 615 700 605 723 585 Z" fill="url(#heroGrad)"/>
  </svg>

  <!-- Header -->
  <header class="site-header">
    <div class="abs brand" style="left:72px;top:14px" aria-label="Clearpath Consulting">
      <span class="brand-dot"></span><span>clearpath</span>
    </div>
    <nav class="abs nav" aria-label="Main">
      <a class="active" style="left:0">Home</a>
      <a style="left:63px">About</a>
      <a style="left:126px">Portfolio</a>
      <a style="left:207px">Our Services</a>
      <a style="left:313px">Blog</a>
      <a style="left:367px">Contact Us</a>
    </nav>
    <span class="abs social navy" style="left:863px;top:17px" aria-label="Social profile"></span>
    <span class="abs social blue" style="left:905px;top:17px" aria-label="Social profile"></span>
    <a class="abs btn navy" style="left:970px;top:17px;width:156px;height:35px">Start Your Project</a>
  </header>

  <!-- Hero text -->
  <section class="hero">
    <p class="abs hero-kicker">Clearpath Consulting</p>
    <h1 class="abs hero-title">Healthcare Marketing<br>Agency</h1>
    <a class="abs btn blue" style="left:143px;top:404px;width:128px;height:34px;z-index:2">Contact Us</a>
    <svg class="abs" style="left:612px;top:520px;z-index:2" width="12" height="16" viewBox="0 0 12 16" aria-hidden="true"><path d="M6 1 V14 M1 9 L6 14 L11 9" stroke="#f0a23a" stroke-width="1.6" fill="none"/></svg>
  </section>

  <!-- Opportunity -->
  <section>
    <div class="abs frame" style="left:165px;top:607px;width:284px;height:328px"></div>
    <div class="abs frame-l" style="left:165px;top:607px;height:22px"></div>
    <div class="abs photo" style="left:143px;top:628px;width:285px;height:330px;background:linear-gradient(135deg,#2e4a78,#b6a99a 55%,#e8a24a)" role="img" aria-label="Photo of hands reviewing website wireframe sketches"></div>
    <h2 class="abs section-title" style="left:496px;top:626px">Don’t miss a new opportunity to grow you<br>practice with your online presence.</h2>
    <div class="abs rule" style="left:496px;top:723px"></div>
    <p class="abs" style="left:564px;top:713px;font-size:16.5px;font-weight:500;color:var(--ink)">Being online: a large opportunity for your practice</p>
    <ul class="abs ticks" style="left:564px;top:760px">
      <li style="top:0"><svg width="14" height="9" viewBox="0 0 14 9"><path d="M1 4 L4 7 L9 1 M5 5 L7 7 L13 1" stroke="#0ba3e3" stroke-width="1.4" fill="none"/></svg>80% of internet uses search for health information</li>
      <li style="top:26px"><svg width="14" height="9" viewBox="0 0 14 9"><path d="M1 4 L4 7 L9 1 M5 5 L7 7 L13 1" stroke="#0ba3e3" stroke-width="1.4" fill="none"/></svg>50% would like information about a specific health professional</li>
      <li style="top:52px"><svg width="14" height="9" viewBox="0 0 14 9"><path d="M1 4 L4 7 L9 1 M5 5 L7 7 L13 1" stroke="#0ba3e3" stroke-width="1.4" fill="none"/></svg>42% of individuals look at health related consumer reviews</li>
      <li style="top:78px"><svg width="14" height="9" viewBox="0 0 14 9"><path d="M1 4 L4 7 L9 1 M5 5 L7 7 L13 1" stroke="#0ba3e3" stroke-width="1.4" fill="none"/></svg>41% of consumers say online presence may impact their choice of health professional</li>
    </ul>
    <p class="abs" style="left:564px;top:882px;font-size:11px;font-weight:600;color:var(--navy);text-decoration:underline"><span style="color:#f0a23a">*</span>Content Sources</p>
    <a class="abs btn blue" style="left:564px;top:926px;width:129px;height:35px">Contact Us</a>
    <a class="abs btn navy" style="left:707px;top:926px;width:157px;height:35px">Start Your Project</a>
  </section>

  <!-- Helping those who help -->
  <section>
    <h2 class="abs section-title" style="left:143px;top:1033px">Clearpath Consulting: helping those<br>who help others.</h2>
    <div class="abs rule" style="left:143px;top:1126px"></div>
    <p class="abs copy" style="left:210px;top:1115px;width:545px">You became a health professional because you wanted to make a difference and you obviously care about patient outcomes. At first things were great and you had plenty of patients but in the last few years there's more competition offering the same types of services and products that you do. Regular customers haven't come back to you in a while and you know you NEED to do something but the old ways like relying on word of mouth doesn't seem to be working well anymore and you don't know how to get started. But that's where we can help... Clearpath Consulting specialises in helping health professionals like you to create a great online user experience for your patients.</p>
    <p class="abs copy" style="left:210px;top:1308px;width:545px">We help you build your online assets through Website development, social media marketing, Online Traffic Strategies.</p>
    <a class="abs btn blue" style="left:210px;top:1377px;width:128px;height:35px">Contact Us</a>
    <a class="abs btn navy" style="left:353px;top:1377px;width:157px;height:35px">Start Your Project</a>
  </section>

  <!-- Since 2015 -->
  <section>
    <div class="abs frame" style="left:165px;top:1483px;width:284px;height:328px"></div>
    <div class="abs frame-l" style="left:165px;top:1483px;height:22px"></div>
    <div class="abs photo" style="left:143px;top:1506px;width:285px;height:328px;background:linear-gradient(120deg,#d9b08a,#a9623f 45%,#3b3f4e 80%)" role="img" aria-label="Photo of two business people shaking hands"></div>
    <h2 class="abs section-title" style="left:496px;top:1502px">Helping clients since 2015:</h2>
    <div class="abs rule" style="left:496px;top:1569px"></div>
    <p class="abs copy-sm" style="left:564px;top:1560px;width:492px">Clearpath consulting specialises in helping health professionals like you, stand out from the busy crowd, find new patient and helps you be seen as the go-to person within your industry. Unlike most health professionals who solely rely on word of mouth, we use the latest online marketing techniques to grow you and your practice.</p>
    <p class="abs copy-sm" style="left:564px;top:1645px;width:492px">While our niche has always been in the healthcare industry, Clearpath Marketing also has experience in providing solutions our e-commerce partners as well as other professional industries.</p>
    <ul class="abs ticks" style="left:564px;top:1706px">
      <li style="top:0"><svg width="14" height="9" viewBox="0 0 14 9"><path d="M1 4 L4 7 L9 1 M5 5 L7 7 L13 1" stroke="#0ba3e3" stroke-width="1.4" fill="none"/></svg>63% Healthcare and medical</li>
      <li style="top:26px"><svg width="14" height="9" viewBox="0 0 14 9"><path d="M1 4 L4 7 L9 1 M5 5 L7 7 L13 1" stroke="#0ba3e3" stroke-width="1.4" fill="none"/></svg>25% ecommerce projects</li>
      <li style="top:52px"><svg width="14" height="9" viewBox="0 0 14 9"><path d="M1 4 L4 7 L9 1 M5 5 L7 7 L13 1" stroke="#0ba3e3" stroke-width="1.4" fill="none"/></svg>12% other professional services</li>
    </ul>
    <a class="abs btn blue" style="left:564px;top:1799px;width:129px;height:35px">Contact Us</a>
    <a class="abs btn navy" style="left:707px;top:1799px;width:157px;height:35px">Start Your Project</a>
  </section>

  <!-- Testimonials -->
  <section>
    <h2 class="abs section-title" style="left:0;width:1200px;text-align:center;top:1911px">See what our clients say</h2>
    <div class="abs quote-ring" style="left:559px;top:1972px"><div class="quote-core">
      <svg width="28" height="20" viewBox="0 0 28 20" aria-hidden="true"><path d="M2 20 V10 C2 4 5 1 11 0 V4 C8 5 7 7 7 9 H12 V20 Z M16 20 V10 C16 4 19 1 25 0 V4 C22 5 21 7 21 9 H26 V20 Z" fill="#fff"/></svg>
    </div></div>
    <p class="abs" style="left:215px;width:770px;top:2075px;text-align:center;font-size:13px;line-height:25.5px;font-style:italic;color:var(--body)">“Lorem Ipsum is simply dummy text of the printing and typesetting industry. Lorem Ipsum has been the industry’s standard dummy text ever since the 1500s, when an unknown printer took a galley of type and scrambled it to make a type specimen book. It has survived not only five centuries. ”</p>
    <p class="abs" style="left:0;width:1200px;top:2173px;text-align:center;font-size:13px;font-weight:600;color:var(--ink)">Mara Quill</p>
    <p class="abs" style="left:0;width:1200px;top:2190px;text-align:center;font-size:13px;color:var(--body)">Lorem Ipsum</p>
    <span class="abs dot" style="left:546px;top:2233px"></span>
    <span class="abs dot on" style="left:570px;top:2233px"></span>
    <span class="abs dot" style="left:594px;top:2233px"></span>
    <span class="abs dot" style="left:617px;top:2233px"></span>
    <span class="abs dot" style="left:641px;top:2233px"></span>
  </section>

  <!-- FAQ -->
  <section>
    <h2 class="abs section-title" style="left:0;width:1200px;text-align:center;top:2314px">Frequently asked questions</h2>
    <div class="abs faq" style="top:2375px;height:232px;border-top:1px solid #e3e5ea">
      <div class="faq-row" style="top:0;height:43px"><span>Lorem Ipsum is simply dummy text of the printing?</span><span class="faq-plus">+</span></div>
      <div class="faq-row faq-open" style="top:43px;height:100px;display:block;border-bottom:none">
        <div style="display:flex;justify-content:space-between"><span>It is a long established fact that a reader?</span><span style="font-size:20px;line-height:14px">−</span></div>
        <p style="font-size:10.4px;line-height:15.5px;font-weight:400;margin-top:8px">There are many variations of passages of Lorem Ipsum available, but the majority have suffered alteration in some form, by injected humour, or randomised words which don't look even slightly believable. If you are going to use a passage of Lorem Ipsum, you need to be sure there isn't anything embarrassing hidden.</p>
      </div>
      <div class="faq-row" style="top:143px;height:44px"><span>There are many variations of passages?</span><span class="faq-plus">+</span></div>
      <div class="faq-row" style="top:187px;height:44px"><span>Contrary to popular belief, Lorem Ipsum is not?</span><span class="faq-plus">+</span></div>
    </div>
  </section>

  <!-- Articles -->
  <section>
    <h2 class="abs section-title" style="left:0;width:1200px;text-align:center;top:2670px">Recent Articles</h2>

    <article class="abs" style="left:143px;top:2732px;width:285px;height:321px">
      <div class="card-img" style="background:linear-gradient(135deg,#e9eef3,#c7cdd6 50%,#f2d2bd)" role="img" aria-label="Photo of hands typing on a laptop keyboard"></div>
      <div class="card-body"><h3 class="card-title">Lorem Ipsum simply</h3><p class="card-text">There are many variations of passages of Lorem Ipsum available, but the majority have ...</p></div>
    </article>
    <article class="abs" style="left:457px;top:2732px;width:285px;height:321px">
      <div class="card-img" style="background:linear-gradient(135deg,#2e4a78,#b6a99a 55%,#e8a24a)" role="img" aria-label="Photo of hands reviewing website wireframe sketches"></div>
      <div class="card-body"><h3 class="card-title">Lorem Ipsum simply</h3><p class="card-text" style="text-decoration:underline">There are many variations of passages of Lorem Ipsum available, but the majority have ...</p></div>
    </article>
    <article class="abs" style="left:771px;top:2732px;width:285px;height:321px">
      <div class="card-img" style="background:linear-gradient(135deg,#a9c9d8,#e6eef3 50%,#3f87b4)" role="img" aria-label="Photo of a doctor with digital health devices on screen"></div>
      <div class="card-body"><h3 class="card-title">Lorem Ipsum simply</h3><p class="card-text">There are many variations of passages of Lorem Ipsum available, but the majority have ...</p></div>
    </article>

    <a class="abs btn blue" style="left:536px;top:3090px;width:128px;height:35px">View All</a>
  </section>

  <!-- Footer -->
  <footer class="abs footer">
    <div class="abs brand" style="left:143px;top:75px;color:var(--white)" aria-label="Clearpath Consulting">
      <span class="brand-dot" style="background:var(--white)"></span><span>clearpath</span>
    </div>
    <p class="abs" style="left:143px;top:150px;font-size:17px;display:flex;align-items:center;gap:8px">
      <svg width="13" height="13" viewBox="0 0 24 24" aria-hidden="true"><path d="M6.6 10.8c1.4 2.8 3.8 5.1 6.6 6.6l2.2-2.2c.3-.3.7-.4 1-.2 1.1.4 2.3.6 3.6.6.6 0 1 .4 1 1V20c0 .6-.4 1-1 1C10.6 21 3 13.4 3 4c0-.6.4-1 1-1h3.5c.6 0 1 .4 1 1 0 1.3.2 2.5.6 3.6.1.3 0 .7-.2 1z" fill="#0ba3e3"/></svg>+100-555-0142</p>
    <p class="abs" style="left:143px;top:179px;font-size:12.5px;display:flex;align-items:center;gap:8px">
      <svg width="13" height="11" viewBox="0 0 24 20" aria-hidden="true"><rect x="1" y="2" width="22" height="16" rx="2" fill="#0ba3e3"/><path d="M2 4 L12 11 L22 4" stroke="#252b4f" stroke-width="2" fill="none"/></svg>hello@clearpathconsulting.example</p>
    <span class="abs social" style="left:145px;top:219px;background:#343b67" aria-label="Social profile"></span>
    <span class="abs social blue" style="left:187px;top:219px" aria-label="Social profile"></span>

    <h3 class="abs foot-head" style="left:457px;top:88px">Quick Links</h3>
    <ul class="abs foot-links" style="left:457px;top:146px;list-style:none">
      <li>Home</li><li>About</li><li>Portfolio</li><li>Our Services</li><li>Blog</li><li>Contact Us</li>
    </ul>
    <ul class="abs foot-links" style="left:561px;top:146px;list-style:none">
      <li>Privacy Policy</li><li>Terms and conditions</li>
    </ul>

    <h3 class="abs foot-head" style="left:754px;top:88px">Subscribe Us</h3>
    <div class="abs" style="left:754px;top:141px;width:302px;height:35px;border-radius:18px;background:#3b4270;font-size:11.5px;color:#d5d8e6;padding:11px 16px">Enter your email...</div>
    <a class="abs btn blue" style="left:754px;top:192px;width:114px;height:35px">Submit</a>

    <p class="abs" style="left:143px;top:344px;font-size:11.5px;color:#e5e7f0">© 2021 <span style="color:var(--blue)">Clearpath Consulting.</span> All rigth reserved.</p>
    <span class="abs" style="left:1119px;top:342px;width:19px;height:19px;border-radius:50%;background:var(--blue);display:flex;align-items:center;justify-content:center">
      <svg width="9" height="6" viewBox="0 0 9 6" aria-hidden="true"><path d="M0 6 L4.5 0 L9 6 Z" fill="#252b4f"/></svg>
    </span>
  </footer>

</main>
</body>
</html>
```